Imported Fine Wine E-commerce site

We need an e-commerce site built from scratch. We currently have a website however it is on Magento and would like a more user friendly platform. Not sure if its possible to use any of the information. We're looking for a mostly white clean design with some red to match the logo.

Target Market(s)

30+

Coding

Coded - Design and coding required

Number of Pages Required

5+ page

Colors
ec1f27

Requirements
Must have
• Categories 'Red/White/Bubbles/Mixed cases/Gifts/Wholesale'
'sort by' functions.
Contact us form
Filter by on left hand side, Variety, Price, Region
Mobile friendly
Must be on a platform that i can update and make changes to it myself

```html
<!DOCTYPE html>
<html lang="en">
<head>
<meta charset="utf-8">
<title>Corvina Cellar – Product Details</title>
<link href="https://fonts.googleapis.com/css2?family=Marcellus&family=Lora:wght@400;500;600&display=swap" rel="stylesheet">
<style>
:root{
  --red:#b01e2d;
  --gold:#8b6a2e;
  --ink:#2b2624;
  --muted:#6b6461;
  --line:#e3ddd6;
  --cream:#f6ece0;
  --hero:#f1ece4;
  --footer:#1f1c1d;
  --footer-text:#d9d3cf;
  --star:#f2a312;
}
*{box-sizing:border-box;margin:0;padding:0}
html,body{width:1200px;height:3102px;overflow:hidden;background:#fff}
body{position:relative;font-family:'Lora',serif;color:var(--ink);font-size:15px}
.abs{position:absolute}
.serif-title{font-family:'Marcellus',serif}
svg{display:block}

/* top bar */
.topbar{top:14px;left:133px;right:134px;height:18px;font-size:12px;color:var(--ink)}
.topbar .item{position:absolute;top:0;display:flex;align-items:center;gap:7px}
.topbar .icon{width:11px;height:11px;fill:var(--gold)}
.top-rule{top:47px;height:1px;background:var(--line)}
.nav{top:85px;font-size:13px;letter-spacing:1px;text-transform:uppercase}
.nav a{position:absolute;color:var(--ink);text-decoration:none;white-space:nowrap}
.nav a.active{color:var(--red)}
.logo-disc{left:498px;top:-2px;width:204px;height:204px;border-radius:50%;background:#fff;z-index:3;box-shadow:0 2px 6px rgba(0,0,0,.05)}
.logo{left:498px;top:70px;width:204px;z-index:4;text-align:center;font-family:'Marcellus',serif;font-size:30px;color:var(--ink);line-height:1}
.logo small{display:block;font-size:17px;letter-spacing:5px;margin-top:4px;color:var(--ink)}
.logo-dot{left:589px;top:42px;width:22px;height:22px;border-radius:50%;border:2px solid var(--red);z-index:4}

/* hero */
.hero{top:141px;left:0;width:1200px;height:244px;background:var(--hero);border-bottom:1px solid var(--line)}
.hero h1{position:absolute;left:133px;top:62px;font-family:'Marcellus',serif;font-weight:400;font-size:58px;color:var(--gold)}
.hero p{position:absolute;left:133px;top:130px;width:440px;font-size:14.5px;line-height:22px}
.crumbs{position:absolute;left:133px;top:216px;font-size:13px;display:flex;gap:14px}
.crumbs .here{color:var(--red)}
.hero-art{position:absolute;left:794px;top:15px;width:272px;height:228px;border-radius:4px;background:linear-gradient(135deg,#7b1620 0%,#a33038 35%,#e8d690 60%,#5d8a2a 100%)}
.follow{position:absolute;left:30px;top:188px;transform:rotate(-90deg);transform-origin:left top;font-size:12px;white-space:nowrap;color:var(--ink)}
.social-v{position:absolute;left:39px;top:48px;display:flex;flex-direction:column;gap:11px}
.social-v span{width:9px;height:9px;border-radius:2px;background:#c4a590}
.social-v span.on{background:var(--red);border-radius:50%}

/* product */
.thumb{left:133px;width:80px;height:102px;background:var(--cream);border:1px solid var(--line)}
.thumb.sel{border:3px solid #efe3d1}
.thumb .bottle{position:absolute;left:50%;bottom:12px;transform:translateX(-50%)}
.main-img{left:227px;top:454px;width:441px;height:472px;background:var(--cream)}
.bottle-shape{position:absolute}
.heart{position:absolute;right:22px;top:20px}
.cat{left:692px;top:450px;color:var(--red);font-size:14px}
.p-title{left:692px;top:482px;font-family:'Marcellus',serif;font-size:30px;color:var(--gold);white-space:nowrap}
.rating{left:692px;top:530px;display:flex;align-items:center;gap:6px;font-size:14px}
.stars{display:flex;gap:1px}
.rule{height:1px;background:var(--line)}
.price{left:692px;top:590px;font-size:21px;display:flex;gap:14px}
.price s{color:var(--muted)}
.price .now,.card .now{color:var(--red)}
.desc{left:692px;top:658px;width:374px;font-size:14.5px;line-height:22px}
.qty{left:692px;top:763px;width:135px;height:47px;border:1px solid var(--line);display:flex;align-items:center;justify-content:space-between;padding:0 18px;font-size:16px}
.qty b{font-size:20px;font-weight:600}
.btn-red{background:var(--red);color:#fff;display:flex;align-items:center;justify-content:center;gap:10px;letter-spacing:1px;text-transform:uppercase;font-size:13px}
.add-cart{left:840px;top:763px;width:176px;height:47px;font-weight:600}
.meta{left:692px;font-size:13px;letter-spacing:.5px}
.meta span{color:var(--red);margin-left:6px}

/* tabs & review */
.tabs{top:1015px;font-size:16px}
.tabs div{position:absolute;white-space:nowrap}
.tabs .active{color:var(--red)}
.tab-line{position:absolute;top:10px;width:26px;height:1px;background:var(--red)}
.avatar{left:213px;top:1087px;width:132px;height:132px;border-radius:50%;background:radial-gradient(circle at 50% 40%,#cfc6bd,#a7b8c9);border:4px solid #f1ece6}
.rev-date{left:373px;top:1094px;font-size:13px;color:var(--red)}
.rev-name{left:373px;top:1115px;font-size:17px;letter-spacing:.3px}
.rev-text{left:373px;top:1145px;width:610px;font-size:14.5px;line-height:22px;color:#3c3634}
.add-review{top:1292px;left:0;width:1200px;text-align:center;font-size:21px;color:var(--red);font-family:'Lora',serif}
.center-text{left:0;width:1200px;text-align:center;font-size:14px;line-height:22px;padding:0 210px}
.field{border:1px solid #d5cfca;font-size:13px;color:var(--muted);padding:12px 15px}
.check{left:369px;top:1626px;display:flex;align-items:center;gap:10px;font-size:11.5px;color:var(--muted)}
.check i{width:12px;height:12px;border:1px solid #aaa;display:block}
.submit{left:525px;top:1662px;width:150px;height:48px;letter-spacing:1px}

/* related */
.rel-title{top:1810px;left:0;width:1200px;text-align:center;font-family:'Marcellus',serif;font-size:44px;color:var(--gold)}
.card{top:1949px;width:295px}
.card .img{height:410px;background:var(--cream);position:relative}
.card .img.light{background:#f7f4ef}
.card .badge{position:absolute;left:20px;top:20px;border:1px solid var(--line);background:#fff;color:var(--red);font-size:12px;padding:3px 11px}
.card .cat2{margin-top:22px;text-align:center;color:var(--gold);font-size:14px}
.card .name{margin-top:10px;text-align:center;font-size:14.5px;letter-spacing:1px;text-transform:uppercase}
.card .pr{margin-top:10px;text-align:center;font-size:21px;display:flex;justify-content:center;gap:14px}
.card .pr s{color:var(--muted)}

/* newsletter */
.news{top:2531px;left:0;width:1200px;height:139px;background:var(--red);color:#fff}
.news h2{position:absolute;left:133px;top:28px;font-family:'Marcellus',serif;font-weight:400;font-size:29px}
.news p{position:absolute;left:133px;top:68px;width:450px;font-size:14.5px;line-height:22px}
.news .email{position:absolute;left:622px;top:49px;width:287px;height:40px;background:#fff;color:var(--red);font-size:13px;padding:11px 20px}
.news .sub{position:absolute;left:916px;top:49px;width:150px;height:40px;background:#231f20;color:#fff;font-size:13px;letter-spacing:1px;font-weight:600;display:flex;align-items:center;justify-content:center}
.news .grapes{position:absolute;right:0;top:0;width:135px;height:139px;background:linear-gradient(110deg,rgba(176,30,45,0) 0%,#5c1a2a 40%,#4f6b2a 100%)}

/* footer */
.footer{top:2670px;left:0;width:1200px;height:432px;background:var(--footer);color:var(--footer-text)}
.f-logo{position:absolute;left:133px;top:108px;font-family:'Marcellus',serif;font-size:32px;color:#fff;line-height:1}
.f-logo small{display:block;font-size:17px;letter-spacing:5px;margin-top:5px}
.f-logo-dot{position:absolute;left:133px;top:76px;width:22px;height:22px;border-radius:50%;border:2px solid #fff}
.f-about{position:absolute;left:133px;top:210px;width:210px;font-size:14px;line-height:20px}
.f-follow{position:absolute;left:133px;top:282px;font-size:14px}
.f-social{position:absolute;left:133px;top:313px;display:flex;gap:18px}
.f-social span{width:11px;height:11px;border-radius:2px;background:#c4a590}
.col{position:absolute;top:108px;font-size:14.5px}
.col h3{font-family:'Lora',serif;font-weight:400;font-size:17px;color:#c99a5c}
.col .dash{width:22px;height:1px;background:#c99a5c;margin:16px 0 11px}
.col a{display:block;color:var(--footer-text);text-decoration:none;line-height:29px}
.col p{line-height:19px;margin-bottom:18px}
.f-bottom{position:absolute;left:0;top:379px;width:1200px;height:1px;background:#3a3536}
.copy{position:absolute;left:133px;top:397px;font-size:12px;color:#9d9590}
.f-links{position:absolute;right:134px;top:397px;font-size:12px;color:#9d9590;display:flex;gap:18px}
</style>
</head>
<body>

<!-- Top bar -->
<div class="abs topbar">
  <div class="item" style="left:0">
    <svg class="icon" viewBox="0 0 24 24"><path d="M6.6 10.8a15 15 0 0 0 6.6 6.6l2.2-2.2c.3-.3.7-.4 1-.2 1.1.4 2.3.6 3.6.6.6 0 1 .4 1 1V20c0 .6-.4 1-1 1A17 17 0 0 1 3 4c0-.6.4-1 1-1h3.5c.6 0 1 .4 1 1 0 1.3.2 2.5.6 3.6.1.3 0 .7-.2 1z"/></svg>
    Call us: 555-012-3490
  </div>
  <div class="item" style="left:155px">
    <svg class="icon" viewBox="0 0 24 24"><path d="M2 5h20v14H2z"/><path d="M2 5l10 8 10-8" stroke="#fff" stroke-width="2" fill="none"/></svg>
    hello@corvinacellar.com
  </div>
  <div class="item" style="left:625px">
    <svg class="icon" viewBox="0 0 24 24"><path d="M3 9h18l-2 11H5z M7 9l3-6 M17 9l-3-6" stroke="#8b6a2e" stroke-width="2"/></svg>
    Your Cart:&nbsp; 0 items - $0.00
  </div>
  <div class="item" style="left:835px;color:#bbb">|</div>
  <div class="item" style="left:862px">
    <svg class="icon" viewBox="0 0 24 24" style="fill:none;stroke:#b01e2d;stroke-width:3"><circle cx="10" cy="10" r="6"/><path d="M15 15l6 6"/></svg>
    Search...
  </div>
</div>
<div class="abs top-rule" style="left:133px;width:373px"></div>
<div class="abs top-rule" style="left:694px;width:372px"></div>

<nav class="abs nav">
  <a style="left:230px">Home</a>
  <a style="left:314px">Features</a>
  <a class="active" style="left:425px">Store</a>
  <a style="left:731px">Wine List</a>
  <a style="left:845px">Blog</a>
  <a style="left:925px">Contacts</a>
</nav>

<div class="abs logo-disc"></div>
<div class="abs logo-dot"></div>
<div class="abs logo">CORVINA<small>CELLAR</small></div>

<!-- Hero -->
<section class="abs hero">
  <div class="social-v"><span></span><span></span><span class="on"></span><span></span></div>
  <div class="follow" style="top:198px">Follow us:</div>
  <h1>Products Details!</h1>
  <p>Quisque at scelerisque magna.Maecenas erat lectus mattis in diam maximus hendrerit malesuada online.</p>
  <div class="crumbs"><span>Home</span><span>›</span><span>Store</span><span>›</span><span class="here">Cabernet Sauvignon</span></div>
  <div class="hero-art" role="img" aria-label="Glasses of red and white wine with green grapes"></div>
</section>

<!-- Product gallery -->
<div class="abs thumb sel" style="top:454px" role="img" aria-label="Red wine bottle thumbnail"></div>
<div class="abs thumb" style="top:578px;background:#e6d8cc" role="img" aria-label="Bottle label close-up"></div>
<div class="abs thumb" style="top:700px;background:#efe4d6" role="img" aria-label="Bottle neck close-up"></div>
<div class="abs thumb" style="top:824px" role="img" aria-label="Bottle side view"></div>

<div class="abs main-img">
  <div class="bottle-shape" role="img" aria-label="Bottle of red wine" style="left:168px;top:33px;width:105px;height:410px;border-radius:40px 40px 10px 10px;background:linear-gradient(90deg,#2a1e20,#3d2a2c 45%,#1c1415)"></div>
  <svg class="heart" width="24" height="22" viewBox="0 0 24 22"><path d="M12 20S2 13.5 2 7.2A5 5 0 0 1 12 5a5 5 0 0 1 10 2.2C22 13.5 12 20 12 20z" fill="none" stroke="#b01e2d" stroke-width="1.8"/></svg>
</div>

<!-- Product info -->
<div class="abs cat">Red Wine</div>
<div class="abs p-title">Luctuson Chardonnayy</div>
<div class="abs rating">
  <div class="stars">
    <svg width="68" height="12" viewBox="0 0 68 12"><g fill="#f2a312"><path id="s" d="M6 0l1.8 3.8 4.2.5-3.1 2.9.8 4.1L6 9.3 2.3 11.3l.8-4.1L0 4.3l4.2-.5z"/><use href="#s" x="14"/><use href="#s" x="28"/><use href="#s" x="42"/><use href="#s" x="56"/></g></svg>
  </div>
  ( 05 customer review )
</div>
<div class="abs rule" style="left:692px;top:571px;width:374px"></div>
<div class="abs price"><s>$85.00</s><span class="now">$65.00</span></div>
<div class="abs rule" style="left:692px;top:638px;width:374px"></div>
<div class="abs desc">Quisque viverra mi nec est egestas lobortis. Mauris purus eros hendrerit et blandit non sodales sed justo. Lorem ipsum dolor sit amet consectetur adipiscing elit. Aenean volutpat velit gravida.</div>
<div class="abs qty"><b>−</b><span>05</span><b style="color:var(--red)">+</b></div>
<div class="abs btn-red add-cart">
  <svg width="14" height="12" viewBox="0 0 24 20"><path d="M2 7h20l-2 12H4z" fill="#fff"/><path d="M7 7l3-6M17 7l-3-6" stroke="#fff" stroke-width="2"/></svg>
  Add to cart
</div>
<div class="abs rule" style="left:692px;top:834px;width:374px"></div>
<div class="abs meta" style="top:857px">SKU: <span>02</span></div>
<div class="abs meta" style="top:880px">CATEGORY: <span>RED WINE</span></div>

<!-- Tabs -->
<div class="abs rule" style="left:133px;top:996px;width:933px"></div>
<div class="abs tabs">
  <div style="left:316px">Product Description</div>
  <div style="left:548px">Additional information</div>
  <div class="tab-line" style="left:761px"></div>
  <div class="active" style="left:799px">Reviews (5)</div>
  <div class="tab-line" style="left:897px"></div>
</div>

<div class="abs avatar" role="img" aria-label="Reviewer portrait"></div>
<div class="abs rev-date">February 22, 2020</div>
<div class="abs rev-name">Martin Ellery</div>
<svg class="abs" style="left:920px;top:1097px" width="68" height="12" viewBox="0 0 68 12"><g fill="#f2a312"><use href="#s"/><use href="#s" x="14"/><use href="#s" x="28"/><use href="#s" x="42"/><use href="#s" x="56"/></g></svg>
<div class="abs rev-text">Quisque viverra mi nec est egestas lobortis. Mauris purus eros hendrerit et blandit non sodales sed justo. Lorem ipsum dolor sit amet consectetur adipiscing elit. Aenean volutpat velit gravida. Donec congue lacinia velit nec tempus.</div>
<div class="abs rule" style="left:133px;top:1258px;width:933px"></div>

<!-- Add review -->
<div class="abs add-review">Add a Review</div>
<div class="abs center-text" style="top:1328px">Quisque viverra mi nec est egestas lobortis. Mauris purus eros hendrerit et blandit non sodales sed justo. Lorem ipsum dolor sit amet consectetur adipiscing elit. Aenean volutpat velit gravida.</div>
<svg class="abs" style="left:566px;top:1387px" width="68" height="12" viewBox="0 0 68 12"><g fill="#cfcac6"><use href="#s"/><use href="#s" x="14"/><use href="#s" x="28"/><use href="#s" x="42"/><use href="#s" x="56"/></g></svg>
<div class="abs field" style="left:292px;top:1430px;width:295px;height:42px">Typw your name here:</div>
<div class="abs field" style="left:613px;top:1430px;width:294px;height:42px">Typw your email here:</div>
<div class="abs field" style="left:292px;top:1494px;width:615px;height:116px">Typw your Review here:</div>
<div class="abs check"><i></i>Save my name, email, and website in this browser for the next time I comment.</div>
<div class="abs btn-red submit">Submit Now</div>
<div class="abs rule" style="left:133px;top:1750px;width:933px"></div>

<!-- Related -->
<div class="abs rel-title">Related Products!</div>
<div class="abs center-text" style="top:1865px;font-size:14.5px">Quisque viverra mi nec est egestas lobortis. Mauris purus eros hendrerit et blandit non sodales sed justo. Lorem ipsum dolor sit amet consectetur adipiscing elit. Aenean volutpat velit gravida.</div>

<div class="abs card" style="left:133px">
  <div class="img"><span class="badge">NEW</span>
    <div class="bottle-shape" role="img" aria-label="Dark red wine bottle" style="left:118px;top:50px;width:62px;height:310px;border-radius:28px 28px 8px 8px;background:linear-gradient(90deg,#1d1717,#352a2b 45%,#141011)"></div>
  </div>
  <div class="cat2">New Arrivals Red Wine</div>
  <div class="name">Luctuson Chardonnayy</div>
  <div class="pr"><s>$85.00</s><span class="now">$65.00</span></div>
</div>
<div class="abs card" style="left:454px">
  <div class="img light">
    <div class="bottle-shape" role="img" aria-label="White wine bottle" style="left:114px;top:32px;width:66px;height:330px;border-radius:28px 28px 8px 8px;background:linear-gradient(90deg,#8d8a2c,#c9c65a 45%,#7a7722)"></div>
  </div>
  <div class="cat2">New Arrivals Red Wine</div>
  <div class="name">Cabernet Sauvignon Reserve</div>
  <div class="pr"><span class="now">$95.00</span></div>
</div>
<div class="abs card" style="left:771px">
  <div class="img">
    <div class="bottle-shape" role="img" aria-label="Sparkling wine bottle" style="left:110px;top:50px;width:76px;height:312px;border-radius:30px 30px 10px 10px;background:linear-gradient(90deg,#0d2313,#1f4a28 45%,#0b1b10)"></div>
  </div>
  <div class="cat2">New Arrivals Red Wine</div>
  <div class="name">Lambert Sweet White</div>
  <div class="pr"><span class="now">$58.00</span></div>
</div>

<!-- Newsletter -->
<section class="abs news">
  <h2>Fresh News from Corvina Cellar Wine</h2>
  <p>Quisque viverra mi nec est egestas lobortis. Mauris purus eros hendrerit et blandit non sodales sed justo.</p>
  <div class="email">Enter your email id</div>
  <div class="sub">SUBSCRIBE NOW</div>
  <div class="grapes" role="img" aria-label="Bunch of red grapes"></div>
</section>

<!-- Footer -->
<footer class="abs footer">
  <div class="f-logo-dot"></div>
  <div class="f-logo">CORVINA<small>CELLAR</small></div>
  <div class="f-about">Quisque viverra mi nec est egestas lobortis. Mauris purus eros hendrerit...</div>
  <div class="f-follow">Follow Us On:</div>
  <div class="f-social"><span></span><span></span><span style="border-radius:50%"></span><span></span></div>

  <div class="col" style="left:400px">
    <h3>Support</h3><div class="dash"></div>
    <a>Contact Us</a><a>About Us</a><a>Careers</a><a>Refunds &amp; Returns</a><a>Deliveries</a>
  </div>
  <div class="col" style="left:652px">
    <h3>Information</h3><div class="dash"></div>
    <a>Search Terms</a><a>Advanced Search</a><a>Help &amp; FAQ's</a><a>Store Location</a><a>Orders &amp; Returns</a>
  </div>
  <div class="col" style="left:908px;width:170px">
    <h3>Contact us</h3><div class="dash"></div>
    <p style="margin-top:6px">Address:</p>
    <p>No: 14 B, West Harbor Lane, Portland, OR</p>
    <p>Phone:<br>USA 5012 +1 555 0147</p>
    <p>Email:<br>hello@corvinacellar.com</p>
  </div>

  <div class="f-bottom"></div>
  <div class="copy">Copyright© corvinacellar 2020 All rights reserved.</div>
  <div class="f-links"><span>Privacy Policy</span><span>Information</span><span>Help</span></div>
</footer>

</body>
</html>
```